■デザインへの要望
1)フライヤーのイメージとしては明るく女性的なイメージを希望します。
2)人物写真は使わないでください。
3)コーポレートロゴを右上に配置してください。
ロゴの改変(色の変更や比率の変更)はご遠慮ください。
4)会のロゴを配置してください。
位置はお任せしますが、サイズの変更はご遠慮ください。
※前回のフライヤーを素材と一緒にお付けしますのでご参考になさってください。

■素材
1)フライヤーを作成する際に必要なロゴ等の画像等は

```html
<!DOCTYPE html>
<html lang="ja">
<head>
<meta charset="utf-8">
<title>ランチョンセミナー15 これからの摂食嚥下障害看護に何が求められているか</title>
<link rel="stylesheet" href="https://fonts.googleapis.com/css2?family=Noto+Sans+JP:wght@400;500;700;900&family=Noto+Serif+JP:wght@500;700&display=swap">
<style>
  :root {
    --navy: #1b2d6b;
    --ink: #2b2b2b;
    --blue: #2e7fc6;
    --blue-deep: #1f5fa8;
    --sky-top: #bfe0f5;
    --sky-mid: #e4f2fb;
    --leaf: #39a34a;
    --rule: #c9dceb;
    --white: #ffffff;
  }
  * { margin: 0; padding: 0; box-sizing: border-box; }
  html, body { width: 849px; height: 1200px; overflow: hidden; background: var(--white); }
  body { font-family: "Noto Sans JP", sans-serif; color: var(--ink); }

  .flyer { position: relative; width: 849px; height: 1200px; overflow: hidden; background: var(--white); }

  .sky {
    position: absolute; left: 0; top: 0; width: 849px; height: 470px;
    background: linear-gradient(180deg, var(--sky-top) 0%, var(--sky-mid) 55%, rgba(255,255,255,0) 100%);
  }

  .society-name { position: absolute; left: 34px; top: 46px; font-size: 15px; font-weight: 700; color: var(--navy); }

  .congress { position: absolute; left: 140px; top: 38px; font-size: 28px; font-weight: 500; color: var(--navy); letter-spacing: 0.5px; }

  .company { position: absolute; right: 34px; top: 22px; font-size: 36px; font-weight: 700; color: var(--leaf); }

  .seminar-band {
    position: absolute; left: 150px; top: 110px; width: 550px; height: 34px;
    background: linear-gradient(90deg, rgba(46,127,198,0) 0%, var(--blue) 18%, var(--blue) 82%, rgba(46,127,198,0) 100%);
    color: var(--white); font-size: 23px; font-weight: 700; text-align: center; line-height: 34px; letter-spacing: 2px;
  }

  .title { display: block; position: absolute; left: 0; width: 849px; text-align: center; font-family: "Noto Serif JP", serif; font-weight: 700; color: var(--navy); letter-spacing: 1px; font-size: 50px; line-height: 1.3; }
  .title.line1 { top: 166px; }
  .title.line2 { top: 236px; }

  .subtitle { position: absolute; left: 0; top: 322px; width: 849px; text-align: center; font-size: 28px; font-weight: 700; color: var(--navy); }
  .english { position: absolute; left: 0; top: 364px; width: 849px; text-align: center; font-size: 19px; font-style: italic; font-weight: 500; color: var(--blue); }

  .date { position: absolute; left: 0; top: 472px; width: 849px; text-align: center; color: var(--navy); font-family: "Noto Serif JP", serif; font-weight: 700; white-space: nowrap; line-height: 1; }
  .date .num { font-size: 42px; }
  .date .big { font-size: 78px; }
  .date .unit { font-size: 36px; }
  .date .dow { display: inline-block; width: 40px; height: 40px; border-radius: 50%; background: var(--navy); color: var(--white); font-size: 24px; line-height: 40px; text-align: center; vertical-align: 6px; margin: 0 8px; }
  .date .time { font-size: 42px; }

  .venue-band {
    position: absolute; left: 80px; top: 578px; width: 690px; height: 30px;
    background: linear-gradient(90deg, var(--blue-deep), var(--blue) 70%, rgba(46,127,198,0.2));
    color: var(--white); font-size: 20px; font-weight: 700; line-height: 30px; padding-left: 14px;
  }
  .venue-band small { font-size: 16px; font-weight: 500; }

  .role { position: absolute; left: 110px; width: 112px; height: 74px; background: linear-gradient(180deg, var(--blue), var(--blue-deep)); color: var(--white); font-size: 28px; font-weight: 700; text-align: center; line-height: 74px; letter-spacing: 6px; }
  .role.chair { top: 644px; }
  .role.speaker { top: 800px; }

  .person { position: absolute; left: 262px; }
  .person .name { font-family: "Noto Serif JP", serif; font-size: 42px; font-weight: 700; color: var(--ink); letter-spacing: 4px; line-height: 1.3; }
  .person .name span { font-size: 24px; letter-spacing: 1px; margin-left: 10px; }
  .person .aff { font-size: 18px; line-height: 1.5; color: var(--ink); }
  .person.chair { top: 640px; }
  .person.speaker { top: 796px; }

  .divider { position: absolute; left: 100px; top: 765px; width: 650px; height: 2px; background: var(--rule); }

  .bokeh { position: absolute; left: 0; top: 960px; width: 849px; height: 170px;
    background: linear-gradient(90deg, rgba(246,178,206,0.55), rgba(255,226,150,0.55) 35%, rgba(172,224,196,0.55) 65%, rgba(168,206,240,0.55));
    -webkit-mask-image: linear-gradient(180deg, transparent, #000 40%, #000 70%, transparent);
            mask-image: linear-gradient(180deg, transparent, #000 40%, #000 70%, transparent);
  }

  .footer { position: absolute; left: 0; top: 1128px; width: 849px; text-align: center; font-size: 14px; line-height: 1.45; color: var(--ink); }
</style>
</head>
<body>
<main class="flyer">
  <div class="sky"></div>

  <p class="society-name">嚥下ケア学会</p>
  <p class="congress">第25回日本嚥下ケア研究学会学術大会</p>

  <p class="company">ハルモア</p>

  <p class="seminar-band">ランチョンセミナー15</p>

  <h1>
    <span class="title line1">これからの摂食嚥下障害看護に</span>
    <span class="title line2">何が求められているか</span>
  </h1>
  <p class="subtitle">〜「機能低下予防」と「終末期care」〜</p>
  <p class="english">What is required in the future for dysphagia nursing</p>

  <p class="date"><span class="num">2019</span><span class="unit">年</span><span class="big">9</span><span class="unit">月</span><span class="big">7</span><span class="unit">日</span><span class="dow">土</span><span class="time">12:00～13:00</span></p>

  <p class="venue-band">第8会場 <small>(白鷺ホール 湊コンベンションセンター 2F 中会議室201)</small></p>

  <div class="role chair">座長</div>
  <div class="person chair">
    <p class="name">山科 春子<span>先生</span></p>
    <p class="aff">瀬戸内看護大学　名誉教授</p>
  </div>

  <div class="divider"></div>

  <div class="role speaker">演者</div>
  <div class="person speaker">
    <p class="name">森川 千里<span>先生</span></p>
    <p class="aff">公益社団法人東海看護協会<br>認定看護師教育課程<br>摂食・嚥下障害看護認定看護師教育課程　主任教員</p>
  </div>

  <div class="bokeh" role="img" aria-label="パステルカラーの柔らかな光の玉の装飾"></div>

  <p class="footer">【共催】<br>第25回日本嚥下ケア研究学会学術大会<br>ハルモア株式会社</p>
</main>
</body>
</html>
```